Potential SF Gazette Best Seller Poetry Book Cover Contest

I’m penning my first poetry book. It’s entitled “Lanterns Under Rain”
I’m fairly open to creative freedom but I want the cover to without a doubt catch a persons' eye instantly because first impressions are VERY IMPORTANT in the literary world
I tend to lean towards a luxury look and colors like black, gold, rose gold, silver, glitter etc but again I’m open to interpretation
Looking forward to your submissions
Target Market(s)
those seeking relatable love advice and quotes
modern millenials
Colors
Look and feel

```html
<!DOCTYPE html>
<html lang="en">
<head>
<meta charset="utf-8">
<title>Lanterns Under Rain — Book Cover</title>
<link rel="stylesheet" href="https://fonts.googleapis.com/css2?family=Josefin+Sans:wght@300;400&family=Yellowtail&family=Permanent+Marker&display=swap">
<style>
  :root {
    --backdrop: #262626;
    --cover: #0c0c0c;
    --crimson: #c8141e;
    --gold: #e9b80f;
    --gold-deep: #b98a06;
    --white: #f7f7f7;
    --subtitle: #d9d9d9;
  }
  * { margin: 0; padding: 0; box-sizing: border-box; }
  html, body {
    width: 1200px;
    height: 1000px;
    overflow: hidden;
    background: var(--backdrop);
  }
  .book-cover {
    position: absolute;
    left: 320px;
    top: 100px;
    width: 560px;
    height: 800px;
    background: var(--cover);
    box-shadow: 0 20px 50px rgba(0,0,0,0.45);
    overflow: hidden;
  }
  .glitter-spray {
    position: absolute;
    left: 60px;
    top: 200px;
    width: 460px;
    height: 300px;
    border-radius: 50%;
    background: radial-gradient(ellipse at 50% 50%, rgba(233,184,15,0.38) 0%, rgba(185,138,6,0.18) 45%, rgba(12,12,12,0) 72%);
  }
  .heart-icon {
    position: absolute;
    left: 296px;
    top: 122px;
    width: 62px;
    height: 54px;
  }
  .title {
    position: absolute;
    left: 0;
    top: 0;
    width: 100%;
  }
  .title-lanterns {
    position: absolute;
    left: 70px;
    top: 178px;
    font-family: "Josefin Sans", sans-serif;
    font-weight: 400;
    font-size: 70px;
    letter-spacing: 2px;
    color: var(--crimson);
    line-height: 1;
  }
  .title-under {
    position: absolute;
    left: 120px;
    top: 246px;
    font-family: "Yellowtail", cursive;
    font-size: 136px;
    color: var(--gold);
    line-height: 1;
    transform: rotate(-6deg);
  }
  .title-rain {
    position: absolute;
    left: 300px;
    top: 376px;
    font-family: "Permanent Marker", cursive;
    font-size: 104px;
    color: var(--white);
    line-height: 1;
  }
  .subtitle {
    position: absolute;
    left: 60px;
    right: 60px;
    top: 660px;
    font-family: "Josefin Sans", sans-serif;
    font-weight: 300;
    font-size: 13px;
    letter-spacing: 3px;
    line-height: 1.6;
    color: var(--subtitle);
    text-align: center;
    text-transform: uppercase;
  }
</style>
</head>
<body>
  <main class="book-cover">
    <div class="glitter-spray" role="img" aria-label="Spray of fine gold glitter behind the title"></div>

    <svg class="heart-icon" viewBox="0 0 62 54" aria-hidden="true">
      <path d="M31 52 C10 36 2 26 2 15 C2 7 8 2 16 2 C23 2 28 6 31 12 C34 6 39 2 46 2 C54 2 60 7 60 15 C60 26 52 36 31 52 Z" fill="var(--crimson)"/>
    </svg>

    <h1 class="title">
      <span class="title-lanterns">LANTERNS</span>
      <span class="title-under">Under</span>
      <span class="title-rain">Rain</span>
    </h1>

    <p class="subtitle">Those seeking relatable love advice and<br>quotes modern millenials</p>
  </main>
</body>
</html>
```